AV & Engineering company needs a Business Card Design

Like the simple design, don't too colorful. Smart & professional feel

• I would like to see the vertical design.

```html
<!DOCTYPE html>
<html lang="en">
<head>
<meta charset="utf-8">
<title>Norvale Systems – Business Card</title>
<link rel="stylesheet" href="https://fonts.googleapis.com/css2?family=Open+Sans:wght@400;600;700&family=Arimo:wght@400;700&display=swap">
<style>
  :root {
    --backdrop: #262626;
    --card: #f7f7f7;
    --card-edge: #e6e6e6;
    --brand-red: #a3161c;
    --slate: #5a5a5a;
    --ink: #1e1e1e;
    --muted: #444444;
  }
  * { box-sizing: border-box; margin: 0; padding: 0; }
  html, body { width: 1200px; height: 873px; overflow: hidden; }
  body {
    background: var(--backdrop);
    font-family: "Arimo", Arial, sans-serif;
    position: relative;
  }
  .card {
    position: absolute;
    top: 156px;
    width: 320px;
    height: 560px;
    background: linear-gradient(160deg, #ffffff 0%, var(--card) 60%, var(--card-edge) 100%);
    overflow: hidden;
    box-shadow: 0 10px 30px rgba(0,0,0,0.5);
  }
  .card--front { left: 250px; }
  .card--back { left: 630px; }

  .card__bands { position: absolute; left: 0; bottom: 0; width: 320px; height: 40px; }

  .wordmark {
    position: absolute;
    left: 0; right: 0;
    display: flex;
    flex-direction: column;
    align-items: center;
    gap: 14px;
    text-align: center;
  }
  .wordmark__mark {
    width: 40px; height: 40px;
    background: var(--brand-red);
    border-radius: 5px;
  }
  .wordmark__name {
    font-family: "Open Sans", sans-serif;
    font-weight: 700;
    color: var(--brand-red);
    font-size: 24px;
    line-height: 1.1;
    letter-spacing: 0.5px;
    text-transform: uppercase;
  }
  .card--front .wordmark { top: 190px; }
  .card--back .wordmark { top: 64px; }

  .tagline {
    position: absolute;
    left: 0; right: 0; top: 338px;
    text-align: center;
    font-family: "Open Sans", sans-serif;
    font-weight: 600;
    font-size: 12px;
    letter-spacing: 3px;
    color: var(--brand-red);
  }

  .holder {
    position: absolute;
    left: 0; right: 0; top: 238px;
    text-align: center;
  }
  .holder__name {
    font-family: "Open Sans", sans-serif;
    font-weight: 700;
    font-size: 18px;
    color: var(--brand-red);
  }
  .holder__role {
    font-weight: 700;
    font-size: 13px;
    color: var(--muted);
    margin-top: 3px;
  }

  .contact-tab {
    position: absolute;
    left: 0; top: 382px;
    width: 40px; height: 100px;
    background: var(--brand-red);
    border-radius: 0 10px 10px 0;
    display: flex;
    flex-direction: column;
    justify-content: space-around;
    align-items: center;
    padding: 4px 0;
  }
  .contact-tab svg { width: 15px; height: 15px; fill: #fff; }

  .contact-list {
    position: absolute;
    left: 52px; top: 382px;
    list-style: none;
    font-size: 13px;
    color: var(--ink);
    line-height: 25px;
  }
</style>
</head>
<body>

  <section class="card card--front" aria-label="Card front">
    <div class="wordmark">
      <span class="wordmark__mark"></span>
      <span class="wordmark__name">Norvale Systems<br>Company Ltd</span>
    </div>
    <p class="tagline">Your Slogan / Tagline Here</p>
    <svg class="card__bands" viewBox="0 0 320 40" preserveAspectRatio="none" aria-hidden="true">
      <path d="M0 28 L170 28 Q182 28 188 18 Q194 8 206 8 L320 8 L320 40 L0 40 Z" fill="var(--slate)"/>
      <path d="M0 30 L174 30 Q186 30 192 22 Q198 14 210 14 L320 14 L320 40 L0 40 Z" fill="var(--brand-red)"/>
    </svg>
  </section>

  <section class="card card--back" aria-label="Card back">
    <div class="wordmark">
      <span class="wordmark__mark"></span>
      <span class="wordmark__name">Norvale Systems<br>Company Ltd</span>
    </div>

    <div class="holder">
      <p class="holder__name">DANIEL MERCER</p>
      <p class="holder__role">Managing Director</p>
    </div>

    <div class="contact-tab" aria-hidden="true">
      <svg viewBox="0 0 16 16"><path d="M2 5 Q8 1 14 5 L12 7 L10 6 L6 6 L4 7 Z M4 8 L12 8 L13 14 L3 14 Z"/></svg>
      <svg viewBox="0 0 16 16"><path d="M1 3 H15 V13 H1 Z M2 4 L8 9 L14 4 Z" fill-rule="evenodd"/></svg>
      <svg viewBox="0 0 16 16"><path d="M2 12 L6 8 L8 10 L4 14 Z M8 6 L12 2 L14 4 L10 8 Z M5 10 L10 5 L11 6 L6 11 Z"/></svg>
      <svg viewBox="0 0 16 16"><path d="M8 1 L15 8 L13 8 L13 15 L10 15 L10 10 L6 10 L6 15 L3 15 L3 8 L1 8 Z"/></svg>
    </div>
    <ul class="contact-list">
      <li>+61 400 217 964</li>
      <li>info@norvalesys.com.au</li>
      <li>www.norvalesys.com.au</li>
      <li>120 Harbour View Rd, Sydney NSW 2000</li>
    </ul>

    <svg class="card__bands" viewBox="0 0 320 40" preserveAspectRatio="none" aria-hidden="true">
      <path d="M0 30 L320 30 L320 40 L0 40 Z" fill="var(--slate)"/>
      <path d="M160 40 Q160 18 182 18 L320 18 L320 40 Z" fill="var(--brand-red)"/>
    </svg>
  </section>

</body>
</html>
```